Vertical flyer design to guide people to my shop

We need a vertical flyer design for a tailor shop, Marlow Stitchers. Our shop is on the 3/F, and we need this flyer/poster to placed on the G/F street level to guide people to take the lifts upstairs. Basically to tell people that, "We are here on 3/F!"

Dimensions ratio: 80 (wide) x200 (tall)

You may use the photos and graphics from the webpages below.
http://www.marlowstitchers.net/en/marlow-stitchers-hong-kong-tailors-tailor-shop/

https://www.fitwerk-q.com/tailor/marlow-stitchers

Industry/Entity Type

Shop

```html
<!DOCTYPE html>
<html lang="en">
<head>
<meta charset="utf-8">
<title>Marlow Stitchers – We Are Here on 3/F</title>
<link rel="stylesheet" href="https://fonts.googleapis.com/css2?family=Libre+Baskerville:ital,wght@0,400;0,700;1,400&display=swap">
<style>
  :root {
    --ink: #111111;
    --black: #0b0b0b;
    --charcoal: #2c2c2c;
    --paper: #ffffff;
    --white-text: #f4f4f4;
    --serif: "Libre Baskerville", Georgia, serif;
  }
  * { box-sizing: border-box; margin: 0; padding: 0; }
  html, body { width: 1200px; height: 2937px; overflow: hidden; background: var(--paper); }
  .flyer { position: relative; width: 1200px; height: 2937px; background: var(--paper); font-family: var(--serif); color: var(--ink); }
  .block { position: absolute; }

  .photo-storefront { left: 0; top: 0; width: 1200px; height: 750px;
    background: linear-gradient(180deg, #1a1714 0%, #3b2f26 45%, #5a4a3c 70%, #2a231e 100%); }
  .title-card { left: 387px; top: 575px; width: 415px; height: 342px; background: var(--paper);
    border: 5px solid var(--ink); display: flex; flex-direction: column; align-items: center; justify-content: center; text-align: center; }
  .title-card .name { font-weight: 700; font-size: 44px; line-height: 1.18; letter-spacing: 1px; text-transform: uppercase; }
  .title-card .tagline { margin-top: 22px; font-size: 24px; line-height: 1.5; text-transform: uppercase; }

  .photo-rack { left: 0; top: 1001px; width: 698px; height: 464px;
    background: linear-gradient(90deg, #0e0e10 0%, #3a3a3c 45%, #6b6660 70%, #1c1c1e 100%); }
  .feature-card { left: 541px; top: 1099px; width: 575px; height: 296px; background: var(--paper);
    border-bottom: 6px solid var(--ink); display: flex; align-items: center; padding-left: 40px; }

  .feature-list { list-style: none; }
  .feature-list li { display: flex; align-items: center; gap: 26px; font-size: 37px; line-height: 1; text-transform: uppercase; margin: 22px 0; }
  .feature-list svg { width: 52px; height: 34px; flex: none; }
  .feature-list.on-dark li { color: var(--white-text); }

  .quality-panel { left: 0; top: 1570px; width: 631px; height: 314px; background: var(--charcoal);
    display: flex; align-items: center; padding-left: 50px; }
  .photo-measure { left: 631px; top: 1570px; width: 569px; height: 314px;
    background: linear-gradient(135deg, #6e6e6e 0%, #a9a9a9 45%, #5d5d5d 100%); }

  .directions { left: 0; top: 1884px; width: 1200px; height: 628px; background: var(--black); color: var(--white-text); }
  .directions .headline { position: absolute; left: 96px; top: 100px; font-weight: 700; font-size: 84px; letter-spacing: 2px; text-transform: uppercase; }
  .directions .instruction { position: absolute; left: 90px; top: 262px; font-size: 50px; line-height: 1.12; text-transform: uppercase; }
  .directions .instruction em { font-style: italic; }
  .directions .floor { position: absolute; left: 104px; top: 470px; font-size: 104px; line-height: 1; }
  .directions .turn-arrow { position: absolute; left: 335px; top: 460px; width: 170px; height: 120px; }
  .photo-jacket { left: 652px; top: 289px; width: 548px; height: 339px;
    background: linear-gradient(120deg, #3b3b3b 0%, #6a6a6a 40%, #242424 100%); }
  .cut-line { position: absolute; left: 0; top: 2512px; width: 1200px; border-top: 6px dashed var(--white-text); }

  .photo-footer { left: 0; top: 2588px; width: 1200px; height: 349px;
    background: linear-gradient(90deg, #1c1c1c 0%, #3c3c3c 40%, #2a2a2a 70%, #4a4a4a 100%);
    display: flex; align-items: center; justify-content: center; }
  .footer-name { color: var(--paper); font-weight: 700; font-size: 58px; line-height: 1.25; text-align: center; text-transform: uppercase; letter-spacing: 1px; }
</style>
</head>
<body>
<main class="flyer">
  <div class="block photo-storefront" role="img" aria-label="Photo of the tailor shop storefront with suits on display in the window"></div>
  <div class="block title-card">
    <div class="name">Marlow<br>Stitchers</div>
    <div class="tagline">Expert Ladies’<br>&amp; Gent’s Tailors</div>
  </div>

  <div class="block photo-rack" role="img" aria-label="Photo of tailored jackets hanging on a rack"></div>
  <div class="block feature-card">
    <ul class="feature-list">
      <li><svg viewBox="0 0 52 34" aria-hidden="true"><path d="M26 4a4 4 0 1 1 0 7v5L3 30h46L26 16" fill="none" stroke="#111" stroke-width="2.5"/></svg>For Ladies’ &amp; Gents’</li>
      <li><svg viewBox="0 0 52 34" aria-hidden="true"><path d="M26 4a4 4 0 1 1 0 7v5L3 30h46L26 16" fill="none" stroke="#111" stroke-width="2.5"/></svg>Best Quality</li>
      <li><svg viewBox="0 0 52 34" aria-hidden="true"><path d="M26 4a4 4 0 1 1 0 7v5L3 30h46L26 16" fill="none" stroke="#111" stroke-width="2.5"/></svg>Expert Tailor</li>
    </ul>
  </div>

  <div class="block quality-panel">
    <ul class="feature-list on-dark">
      <li><svg viewBox="0 0 52 34" aria-hidden="true"><path d="M26 4a4 4 0 1 1 0 7v5L3 30h46L26 16" fill="none" stroke="#f4f4f4" stroke-width="2.5"/></svg>Perfect Fit</li>
      <li><svg viewBox="0 0 52 34" aria-hidden="true"><path d="M26 4a4 4 0 1 1 0 7v5L3 30h46L26 16" fill="none" stroke="#f4f4f4" stroke-width="2.5"/></svg>Luxury</li>
      <li><svg viewBox="0 0 52 34" aria-hidden="true"><path d="M26 4a4 4 0 1 1 0 7v5L3 30h46L26 16" fill="none" stroke="#f4f4f4" stroke-width="2.5"/></svg>Marlow Stitchers</li>
    </ul>
  </div>
  <div class="block photo-measure" role="img" aria-label="Photo of a shirt with a tape measure laid across it"></div>

  <section class="block directions">
    <h1 class="headline">We Are Here !!</h1>
    <p class="instruction">Just turn <em>left</em><br>and press 3/F<br>on the lifts</p>
    <div class="floor">3/F</div>
    <svg class="turn-arrow" viewBox="0 0 170 120" aria-hidden="true">
      <path d="M4 48 L62 6 L62 30 C112 30 158 58 166 114 C146 80 112 66 62 66 L62 90 Z" fill="#f4f4f4"/>
    </svg>
    <div class="block photo-jacket" role="img" aria-label="Close-up photo of a tailored jacket with a tape measure"></div>
  </section>
  <div class="cut-line"></div>

  <div class="block photo-footer" role="img" aria-label="Photo of men wearing tailored suits">
    <div class="footer-name">Marlow<br>Stitchers</div>
  </div>
</main>
</body>
</html>
```